Webdesign für ambulanter Pflegedienst
Zielgruppe
Es ist ein ambulanter Pflegedienst, der sich im Raum Dessau-Roßlau um die Versorgung sowie Betreuung von Menschen kümmert. Kontaktdaten: ambulanter Pflegedienst Hand Sorge; Inhaberin: Sabine Lohmar; Birkenweg 14, 06871 Dessau-Roßlau Telefon: 034907/519364
IK-Nummer: 47 283 6194
e-mail: sl-hand-sorge@postfeld.de
Aufgabenstellung
Die Farben sollen in Anlehnung an das Logo sein, dass mit übersandt wird.

```html
<!DOCTYPE html>
<html lang="de">
<head>
<meta charset="utf-8">
<title>Hand Sorge – Ambulanter Pflegedienst</title>
<link href="https://fonts.googleapis.com/css2?family=Montserrat:wght@500;600;700&family=Raleway:wght@400;500;600&display=swap" rel="stylesheet">
<style>
:root{
  --teal:#4bb3ab;
  --teal-dark:#2f6b68;
  --blue:#2a9fd6;
  --ink:#2d3035;
  --muted:#6b7078;
  --green-soft:#f1fbe2;
  --icon-bg:#eafad6;
  --icon-line:#7cc36a;
  --hero-bg:#eef5f8;
  --badge-bg:#e7f3f8;
  --line:#e3eef0;
  --white:#fff;
}
*{box-sizing:border-box;margin:0;padding:0}
html,body{width:1200px;height:3811px;overflow:hidden;background:var(--white)}
body{position:relative;font-family:"Raleway",sans-serif;color:var(--ink)}
.abs{position:absolute}
h1,h2,h3,.brand{font-family:"Montserrat",sans-serif}
.badge{position:absolute;background:var(--badge-bg);color:var(--blue);font-family:"Montserrat",sans-serif;font-weight:600;font-size:10px;letter-spacing:.08em;padding:6px 9px;border-radius:3px;text-transform:uppercase}
.title{position:absolute;font-weight:600;font-size:22px;line-height:30px;color:var(--ink)}
.text{position:absolute;font-size:10.3px;line-height:17px;color:var(--muted)}
.btn-solid{position:absolute;background:var(--teal);color:#fff;font-family:"Montserrat",sans-serif;font-weight:500;font-size:13px;border-radius:4px;display:flex;align-items:center;justify-content:center}
.btn-line{position:absolute;border:1px solid var(--teal);color:var(--teal);font-size:12px;font-weight:500;border-radius:4px;display:flex;align-items:center;justify-content:center;background:#fff}
.ph{position:absolute}

.header-line{left:45px;top:92px;width:1110px;height:1px;background:var(--line)}
.logo{left:45px;top:30px;display:flex;align-items:center;gap:10px}
.logo-dot{width:34px;height:34px;border-radius:50%;background:var(--teal)}
.logo .brand{font-size:17px;font-weight:500;color:var(--ink)}
.nav{left:332px;top:39px;display:flex;gap:20px;font-family:"Montserrat",sans-serif;font-size:9.5px;font-weight:600;letter-spacing:.05em;color:var(--ink)}
.nav span::before,.foot-list li::before{content:"";display:inline-block;width:5px;height:5px;border-radius:50%;background:var(--blue);margin-right:6px;vertical-align:middle}

.hero-bg{left:30px;top:130px;width:1140px;height:510px;border-radius:0 0 60px 60px;background:linear-gradient(180deg,#fff 0%,var(--hero-bg) 100%)}
.hero-title{left:0;width:1200px;top:185px;text-align:center;font-weight:600;font-size:36px;color:var(--ink)}
.hero-text{left:320px;width:560px;top:246px;text-align:center;font-size:11.5px;line-height:18px;color:var(--muted)}
.qcard{position:absolute;top:558px;width:193px;height:146px;background:#fff;border-radius:14px;box-shadow:0 8px 24px rgba(40,80,90,.1)}
.qcard .ic{position:absolute;left:20px;top:20px;width:70px;height:70px;border-radius:12px;background:var(--icon-bg);display:flex;align-items:center;justify-content:center}
.qcard .lb{position:absolute;left:20px;top:110px;font-size:14px;font-weight:500}
.qcard svg.arr{position:absolute;right:20px;top:112px}

.band{left:0;top:1732px;width:1200px;height:720px;background:var(--green-soft)}
.scard{position:absolute;top:1965px;width:260px;height:337px;background:#fff;border-radius:12px;overflow:hidden;box-shadow:0 6px 18px rgba(60,90,60,.08)}
.scard .img{height:152px}
.scard h3{position:absolute;left:20px;top:172px;font-size:14px;font-weight:600}
.scard .sub{position:absolute;left:20px;top:192px;font-size:11px;color:var(--muted)}
.scard p{position:absolute;left:20px;top:205px;width:220px;font-size:10px;line-height:16px;color:var(--muted)}
.scard .more{position:absolute;left:20px;right:20px;top:295px;display:flex;justify-content:space-between;font-size:10.5px;font-weight:600;color:var(--teal)}
.scard .sep{position:absolute;left:0;right:0;top:278px;height:1px;background:var(--line)}
.navbtn{position:absolute;top:1882px;width:38px;height:38px;border-radius:6px;background:#fff;display:flex;align-items:center;justify-content:center;box-shadow:0 3px 8px rgba(0,0,0,.06)}

.footer{left:0;top:3375px;width:1200px;height:436px;background:var(--teal-dark);color:#fff}
.footer h4{position:absolute;font-family:"Montserrat",sans-serif;font-size:13px;font-weight:600}
.foot-list{position:absolute;list-style:none;font-family:"Montserrat",sans-serif;font-size:9.5px;font-weight:600;letter-spacing:.06em;color:#cfe1df}
.foot-list li{margin-bottom:16px}
.foot-list li::before{background:var(--icon-line)}
.foot-text{position:absolute;font-size:10.5px;line-height:16px;color:#cfe1df}
.dot{position:absolute;border-radius:50%;background:var(--blue)}
</style>
</head>
<body>

<div class="abs logo"><div class="logo-dot"></div><span class="brand">HAND SORGE</span></div>
<nav class="abs nav"><span>HOME</span><span>ÜBER UNS</span><span>SOFORTIGE HILFEN</span><span>UNSERE LEISTUNGEN</span><span>KARRIERE</span><span>PFLEGEKURSE</span></nav>
<div class="btn-solid" style="left:1041px;top:26px;width:70px;height:40px">Kontakt</div>
<div class="abs header-line"></div>

<div class="abs hero-bg"></div>
<div class="badge" style="left:529px;top:145px">Ihr zuverlässiger Partner</div>
<h1 class="abs hero-title">Willkommen im HAND SORGE</h1>
<p class="abs hero-text">Menschliche Betreuung, maßgeschneiderte Pflegepläne und starke Partner für Ihre geliebten<br>Menschen. Lassen Sie uns zusammenarbeiten, um Lebensqualität zu verbessern!</p>
<div class="btn-solid" style="left:554px;top:294px;width:131px;height:40px">Jetzt kontaktieren</div>
<div class="ph" role="img" aria-label="Foto des Pflegeteams in Arbeitskleidung" style="left:265px;top:345px;width:670px;height:295px;background:linear-gradient(180deg,#e9eef1,#c9d6df);border-radius:80px 80px 0 0"></div>

<div class="qcard" style="left:187px"><div class="ic"><svg width="38" height="38" viewBox="0 0 38 38" fill="none" stroke="#7cc36a" stroke-width="2"><circle cx="10" cy="9" r="4"/><circle cx="19" cy="7" r="4"/><circle cx="28" cy="9" r="4"/><path d="M5 32V18h10v14M14 32V16h10v16M23 32V18h10v14"/></svg></div><div class="lb">Über uns</div><svg class="arr" width="16" height="12" viewBox="0 0 16 12" fill="none" stroke="#2b3a67" stroke-width="1.8"><path d="M1 6h13M9 1l5 5-5 5"/></svg></div>
<div class="qcard" style="left:398px"><div class="ic"><svg width="38" height="38" viewBox="0 0 38 38" fill="none" stroke="#7cc36a" stroke-width="2"><rect x="14" y="6" width="18" height="24" rx="2"/><path d="M23 12v8M19 16h8M4 32h10V22H4z"/></svg></div><div class="lb">Sofortige Hilfen</div><svg class="arr" width="16" height="12" viewBox="0 0 16 12" fill="none" stroke="#2b3a67" stroke-width="1.8"><path d="M1 6h13M9 1l5 5-5 5"/></svg></div>
<div class="qcard" style="left:610px"><div class="ic"><svg width="38" height="38" viewBox="0 0 38 38" fill="none" stroke="#7cc36a" stroke-width="2"><path d="M19 22s-8-5-8-10a4 4 0 0 1 8-1 4 4 0 0 1 8 1c0 5-8 10-8 10z"/><path d="M3 20l8 12h16l8-12"/></svg></div><div class="lb">Unsere Leistungen</div><svg class="arr" width="16" height="12" viewBox="0 0 16 12" fill="none" stroke="#2b3a67" stroke-width="1.8"><path d="M1 6h13M9 1l5 5-5 5"/></svg></div>
<div class="qcard" style="left:820px"><div class="ic"><svg width="38" height="38" viewBox="0 0 38 38" fill="none" stroke="#7cc36a" stroke-width="2"><circle cx="17" cy="21" r="11"/><path d="M17 15v12M11 21h12M24 8c3-3 7-3 9 0"/></svg></div><div class="lb">Pflegekurse</div><svg class="arr" width="16" height="12" viewBox="0 0 16 12" fill="none" stroke="#2b3a67" stroke-width="1.8"><path d="M1 6h13M9 1l5 5-5 5"/></svg></div>

<div class="ph" style="left:204px;top:864px;width:300px;height:300px;border-radius:50%;background:#dff0ef"></div>
<div class="ph" role="img" aria-label="Porträtfoto der Gründerin Sabine Lohmar" style="left:262px;top:838px;width:184px;height:235px;border-radius:92px 92px 0 0;background:linear-gradient(180deg,#b8775a,#5a3a30)"></div>
<div class="abs" style="left:215px;top:1072px;width:268px;height:138px;background:#fff;border-radius:8px;box-shadow:0 8px 24px rgba(40,80,90,.12);border-bottom:2px solid var(--teal)">
  <p style="position:absolute;left:24px;top:18px;width:220px;font-size:10px;line-height:14px;color:var(--muted)">Uns ist es wichtig, dass sie ein gutes Gefühl haben, denn nur dann können wir gemeinsam mit ihnen eine sehr gute Pflege gewährleisten.</p>
  <div role="img" aria-label="Handschriftliche Unterschrift" style="position:absolute;left:74px;top:74px;width:124px;height:30px;background:linear-gradient(90deg,#e8eef0,#d9e2e5);border-radius:4px"></div>
  <p style="position:absolute;left:0;width:268px;top:110px;text-align:center;font-size:10px;color:var(--ink)">Eure Sabine Lohmar</p>
</div>
<div class="badge" style="left:616px;top:880px">Über uns und unsere Gründerin</div>
<h2 class="title" style="left:616px;top:916px;width:420px">Sabine Lohmar und Hand Sorge - Ihre Experten für ambulante Pflege</h2>
<p class="text" style="left:616px;top:991px;width:396px">Unter der erfahrenen Leitung unserer Gründerin, Sabine Lohmar, ist Hand Sorge Ihr sicherer Hafen in herausfordernden Zeiten. Wir bieten qualifizierte und einfühlsame Pflege, die es Ihnen ermöglicht, trotz Pflegebedarf zuhause zu leben. Lernen Sie unser umfassendes Angebot kennen und lassen Sie sich von der Herzlichkeit und Expertise unseres Teams beeindrucken. Vertrauen Sie auf die Kompetenz und Empathie von Sabine und ihrem Team. Wir freuen uns auf eine erfolgreiche Zusammenarbeit mit Ihnen.</p>
<div class="btn-line" style="left:616px;top:1140px;width:95px;height:33px">Mehr erfahren</div>

<div class="badge" style="left:187px;top:1301px">Individualisierte Pflege</div>
<h2 class="title" style="left:187px;top:1336px;width:320px">Individualisierte Pflege mit menschlichem Fokus</h2>
<p class="text" style="left:187px;top:1411px;width:420px">Für unseren ambulanten Pflegedienst steht die Pflege von Mensch zu Mensch im Mittelpunkt. Es ist unser Ziel, die Fähigkeiten und Möglichkeiten der Menschen zu erhalten und zu fördern, damit sie ihr Leben so lange wie möglich unabhängig führen und gestalten können. Damit den Pflegebedürftigen eine höchstmögliche Beständigkeit im gesamten Pflegeprozess gewährleistet werden kann, wird ihm eine Bezugsperson zugeordnet. Dies stärkt die Entwicklung von Vertrauen und ermöglicht so eine ganzheitliche Pflege.</p>
<p class="text" style="left:187px;top:1535px;width:420px">Es ist uns wichtig die Angehörigen aktiv in die Gestaltung der Pflege mit einzubeziehen. Dieses Vorhaben wird durch uns in Form von Beratungs-, Anleitungs- und Begleitungsangeboten realisiert.</p>
<div class="btn-line" style="left:187px;top:1610px;width:121px;height:33px">Unsere Leistungen</div>
<div class="ph" role="img" aria-label="Foto einer Familie mit Großmutter und Tulpensträußen" style="left:678px;top:1300px;width:334px;height:340px;border-radius:8px 8px 90px 8px;background:linear-gradient(160deg,#f3e6e0,#d9b4a6 55%,#b6877a)"></div>
<div class="dot" style="left:938px;top:1290px;width:22px;height:22px"></div>
<div class="dot" style="left:656px;top:1565px;width:12px;height:12px"></div>
<div class="dot" style="left:666px;top:1590px;width:26px;height:26px"></div>

<div class="abs band"></div>
<div class="badge" style="left:187px;top:1811px;background:#fff">Das bieten wir an</div>
<h2 class="title" style="left:187px;top:1846px">Unsere Leistungen im Überblick</h2>
<p class="text" style="left:187px;top:1893px;width:540px;font-size:10px">Von der ganzheitlichen Pflege bis zur interdisziplinären Zusammenarbeit - erfahren Sie mehr über unser breites Spektrum an Pflegedienstleistungen, die wir individuell auf Ihre Bedürfnisse zuschneiden.</p>
<div class="navbtn" style="left:922px;opacity:.7"><svg width="10" height="14" viewBox="0 0 10 14" fill="none" stroke="#7a7f86" stroke-width="1.6"><path d="M8 1 2 7l6 6"/></svg></div>
<div class="navbtn" style="left:972px"><svg width="10" height="14" viewBox="0 0 10 14" fill="none" stroke="#2d3035" stroke-width="1.6"><path d="M2 1l6 6-6 6"/></svg></div>

<div class="scard" style="left:187px"><div class="img" role="img" aria-label="Foto einer Pflegerin mit älterem Mann" style="background:linear-gradient(135deg,#e9ecef,#b9c3c9)"></div><h3 style="top:176px">Grundpflege</h3><p style="top:200px">Individuelle Unterstützung im Alltag von Körperpflege bis Mobilität.</p><div class="sep"></div><div class="more"><span>Mehr erfahren</span><span>→</span></div></div>
<div class="scard" style="left:470px"><div class="img" role="img" aria-label="Foto zweier lachender Männer" style="background:linear-gradient(135deg,#d7e3ee,#6e8ca8)"></div><h3>Behandlungspflege</h3><p style="top:195px">Fachpersonal unterstützt den Heilungsprozess und vermeidet Krankenhausaufenthalte.</p><div class="sep"></div><div class="more"><span>Mehr erfahren</span><span>→</span></div></div>
<div class="scard" style="left:752px"><div class="img" role="img" aria-label="Foto eines älteren Paares im Beratungsgespräch" style="background:linear-gradient(135deg,#e6e1da,#a69a8c)"></div><h3>Beratungseinsatz</h3><div class="sub">nach §37 Abs. 3 SGB XI</div><p style="top:210px">Gesetzliche Beratung für Pflegegeldempfänger inklusive Pflegekurse und Entlastung.</p><div class="sep"></div><div class="more"><span>Mehr erfahren</span><span>→</span></div></div>
<div class="scard" style="left:1035px"><div class="img" role="img" aria-label="Foto einer älteren Frau im Pflegebett" style="background:linear-gradient(135deg,#eef0f2,#b5bfc6)"></div><h3>Verhinderungspflege</h3><div class="sub">nach §39 SGB XI</div><p style="top:210px">Stündliche oder rund-um-die-Uhr bei Abwesenheit der Pflegeperson zu Kosten und Antragstellungen.</p><div class="sep"></div><div class="more"><span>Mehr erfahren</span><span>→</span></div></div>

<div class="btn-line" style="left:525px;top:2345px;width:150px;height:33px">Alle Leistungen ansehen</div>

<div class="ph" role="img" aria-label="Foto einer Frau, die einen älteren Mann umarmt" style="left:187px;top:2545px;width:335px;height:340px;border-radius:8px 8px 8px 90px;background:linear-gradient(160deg,#dfe6d3,#9fae86 55%,#7a6a58)"></div>
<div class="dot" style="left:238px;top:2512px;width:14px;height:14px"></div>
<div class="dot" style="left:272px;top:2530px;width:10px;height:10px"></div>
<div class="dot" style="left:242px;top:2542px;width:24px;height:24px"></div>
<div class="dot" style="left:534px;top:2814px;width:12px;height:12px"></div>
<div class="dot" style="left:512px;top:2842px;width:26px;height:26px"></div>
<div class="badge" style="left:581px;top:2577px">Professionelle Zusammenarbeit</div>
<h2 class="title" style="left:581px;top:2612px;width:420px">Interdisziplinäre Zusammenarbeit und Qualitätssicherung</h2>
<p class="text" style="left:581px;top:2688px;width:434px">Eine interdisziplinäre Zusammenarbeit mit Therapeuten, Ärzten und anderen Dienstleistern (dazu gehören Sanitätshäuser, Apotheken, Ärzten und Wundschwestern) trägt zur Erhaltung, Förderung und gegebenenfalls Verbesserung der Lebenssituation des Pflegebedürftigen bei und wird durch uns angestrebt, unterstützt und koordiniert.</p>
<p class="text" style="left:581px;top:2778px;width:434px">Unsere Mitarbeiter bilden die Verbindung zu den Pflegebedürftigen, den Angehörigen und den anderen Professionen und werden entsprechend ihrer Aufgaben sowie beruflichen Qualifikationen intern und extern weitergebildet, um eine höchstmögliche Qualität erreichen zu können. Mit diesem Komplettpaket möchten wir Sie unterstützen den Schicksalsschlag „Pflegebedürftigkeit“ gut bewältigen zu können.</p>

<div class="abs" style="left:187px;top:2977px;width:825px;height:318px;background:var(--hero-bg);border-radius:14px 14px 0 14px;overflow:hidden">
  <div class="ph" role="img" aria-label="Porträtfoto der Inhaberin" style="right:0;bottom:0;width:192px;height:265px;border-radius:96px 96px 0 0;background:linear-gradient(180deg,#b8775a,#3c2a26)"></div>
</div>
<div class="badge" style="left:228px;top:3022px;background:#fff">Kontakt</div>
<h2 class="title" style="left:228px;top:3056px;width:480px">Individuelle Beratung und Unterstützung. Kontaktieren Sie uns.</h2>
<p class="text" style="left:228px;top:3128px;width:460px">Haben Sie Fragen oder benötigen Sie Unterstützung? Unser engagiertes Team ist bereit, Ihnen zu helfen. Kontaktieren Sie uns, um den besten Pflegeweg für Ihre spezielle Situation zu finden. Wir freuen uns auf Sie.</p>
<div class="btn-solid" style="left:228px;top:3215px;width:130px;height:40px">Jetzt kontaktieren</div>
<div class="abs" style="left:383px;top:3222px;font-family:Montserrat,sans-serif;font-weight:600;font-size:20px">034907/519364</div>

<footer class="abs footer">
  <div class="abs" style="left:228px;top:98px;width:70px;height:70px;border-radius:50%;border:2px solid #fff"></div>
  <div class="abs brand" style="left:187px;top:180px;font-size:21px;font-weight:500">HAND SORGE</div>
  <div class="abs" style="left:187px;top:213px;font-size:10px;font-weight:600">Hand Sorge GmbH</div>
  <p class="foot-text" style="left:187px;top:245px;width:170px">Ihr vertrauenswürdiger Pflegedienst, setzt auf individuelle Pflege und persönliche Fürsorge, um ein qualitativ hochwertiges Leben in der eigenen Häuslichkeit zu ermöglichen.</p>

  <h4 style="left:398px;top:103px">Seiten</h4>
  <ul class="foot-list" style="left:398px;top:140px"><li>HOME</li><li>ÜBER UNS</li><li>SOFORTIGE HILFEN</li><li>UNSERE LEISTUNGEN</li><li>KARRIERE</li><li>PFLEGEKURSE</li></ul>

  <h4 style="left:607px;top:103px">Rechtliches</h4>
  <ul class="foot-list" style="left:607px;top:140px"><li>IMPRESSUM</li><li>DATENSCHUTZERKLÄRUNG</li><li>AGB</li></ul>
  <h4 style="left:607px;top:258px">Sonstiges</h4>
  <ul class="foot-list" style="left:607px;top:294px"><li>FAQ</li><li>KONTAKT</li></ul>

  <h4 style="left:816px;top:103px">Kontaktinformationen</h4>
  <p class="foot-text" style="left:816px;top:140px;color:#fff;font-weight:500">Hand Sorge GmbH</p>
  <p class="foot-text" style="left:816px;top:160px">Birkenweg 14<br>06871 Dessau-Roßlau</p>
  <p class="foot-text" style="left:816px;top:206px">034907/519364<br>IK 47 283 6194</p>
  <p class="foot-text" style="left:816px;top:255px;color:var(--icon-line)">sl-hand-sorge@postfeld.de</p>
  <div class="btn-solid" style="left:816px;top:277px;width:117px;height:33px;font-size:11px">Jetzt kontaktieren</div>
</footer>

</body>
</html>
```